Our companies name is The Gilded Ladle and we specialize in craft cupcakes, what I mean by that is that we bake our cupcakes with craft beer and other alcoholic drinks. We are trying to focus on being elegant but at the same time unpretentious. Since we are incorporating beer in our cupcakes we want the business card to have our logo in the front and our information in the back.

Once we select the best design we will provide the contact information to be added. Thank you.

Industry/Entity Type

Business

Font styles to use
Decorative
Script

Requirements
Must have
• Round corners
Should not have
• Square corners

```html
<!DOCTYPE html>
<html lang="en">
<head>
<meta charset="utf-8">
<title>The Gilded Ladle – Business Card</title>
<link rel="stylesheet" href="https://fonts.googleapis.com/css2?family=Michroma&display=swap">
<style>
  :root {
    --backdrop: #e4e1dc;
    --card: #fbfbfb;
    --ink: #1d1d1d;
    --muted: #6a6a6a;
    --accent: #f0562a;
    --edge: #111111;
  }
  html, body {
    margin: 0;
    padding: 0;
    width: 1200px;
    height: 900px;
    overflow: hidden;
    background: var(--backdrop);
    font-family: "Michroma", sans-serif;
  }
  .canvas {
    position: relative;
    width: 1200px;
    height: 900px;
  }
  .card {
    position: absolute;
    left: 280px;
    width: 640px;
    height: 366px;
    border-radius: 36px;
    background: var(--card);
    overflow: hidden;
    box-shadow: 0 6px 20px rgba(0,0,0,0.12);
  }
  .card--front { top: 56px; }
  .card--back { top: 478px; }

  /* Front */
  .wordmark {
    position: absolute;
    inset: 0;
    display: flex;
    align-items: center;
    justify-content: center;
    gap: 18px;
  }
  .wordmark__dot {
    width: 26px;
    height: 26px;
    border-radius: 50%;
    background: var(--accent);
  }
  .wordmark__name {
    font-size: 30px;
    color: var(--ink);
    letter-spacing: 1px;
  }

  /* Back */
  .back-swoosh {
    position: absolute;
    inset: 0;
  }
  .back-logo {
    position: absolute;
    top: 62px;
    left: 250px;
    display: flex;
    align-items: center;
    gap: 10px;
  }
  .back-logo__dot {
    width: 14px;
    height: 14px;
    border-radius: 50%;
    background: var(--accent);
  }
  .back-logo__name {
    font-size: 17px;
    color: var(--ink);
  }
  .identity {
    position: absolute;
    top: 156px;
    right: 340px;
    text-align: right;
  }
  .identity__name {
    font-size: 13px;
    color: var(--accent);
    letter-spacing: 1.5px;
    margin: 0 0 6px;
  }
  .identity__role,
  .identity__address {
    font-size: 10px;
    color: var(--muted);
    letter-spacing: 1px;
    margin: 0 0 5px;
    line-height: 1.55;
  }
  .identity__address { margin-top: 10px; }
  .divider {
    position: absolute;
    top: 150px;
    left: 314px;
    width: 1px;
    height: 120px;
    background: #bdbdbd;
  }
  .contacts {
    position: absolute;
    top: 152px;
    left: 328px;
    margin: 0;
    padding: 0;
    list-style: none;
  }
  .contacts__item {
    display: flex;
    align-items: center;
    gap: 8px;
    height: 22px;
    font-size: 10px;
    color: var(--muted);
    letter-spacing: 1px;
  }
  .contacts__icon {
    width: 14px;
    height: 14px;
    flex: none;
  }
</style>
</head>
<body>
<main class="canvas">

  <section class="card card--front" aria-label="Card front">
    <div class="wordmark">
      <span class="wordmark__dot"></span>
      <span class="wordmark__name">The Gilded Ladle</span>
    </div>
  </section>

  <section class="card card--back" aria-label="Card back">
    <svg class="back-swoosh" width="640" height="366" viewBox="0 0 640 366" aria-hidden="true">
      <path d="M0 0 H40 C10 90 0 250 60 366 H0 Z" fill="var(--edge)"/>
      <path d="M250 14 C120 30 40 110 44 190 C48 260 110 320 200 352" fill="none" stroke="var(--accent)" stroke-width="5" stroke-linecap="round"/>
    </svg>

    <div class="back-logo">
      <span class="back-logo__dot"></span>
      <span class="back-logo__name">The Gilded Ladle</span>
    </div>

    <div class="identity">
      <p class="identity__name">CLARA HALE</p>
      <p class="identity__role">Owner / C.E.O</p>
      <p class="identity__address">Suite # 118, Orin Bldg,<br>NY 40217</p>
    </div>

    <div class="divider"></div>

    <ul class="contacts">
      <li class="contacts__item">
        <svg class="contacts__icon" viewBox="0 0 14 14" aria-hidden="true"><circle cx="7" cy="7" r="7" fill="var(--accent)"/><path d="M4.5 3.5 L6 5 L5.2 6 Q6 8 8 8.8 L9 8 L10.5 9.5 L9.5 10.5 Q6 10.5 3.5 5 Z" fill="#fff"/></svg>
        555-210-4471
      </li>
      <li class="contacts__item">
        <svg class="contacts__icon" viewBox="0 0 14 14" aria-hidden="true"><circle cx="7" cy="7" r="7" fill="var(--accent)"/><path d="M4.5 3.5 L6 5 L5.2 6 Q6 8 8 8.8 L9 8 L10.5 9.5 L9.5 10.5 Q6 10.5 3.5 5 Z" fill="#fff"/></svg>
        555-382-9064
      </li>
      <li class="contacts__item">
        <svg class="contacts__icon" viewBox="0 0 14 14" aria-hidden="true"><circle cx="7" cy="7" r="7" fill="var(--accent)"/><rect x="5" y="3" width="4" height="8" rx="1" fill="#fff"/></svg>
        555-617-2358
      </li>
      <li class="contacts__item">
        <svg class="contacts__icon" viewBox="0 0 14 14" aria-hidden="true"><circle cx="7" cy="7" r="7" fill="var(--accent)"/><rect x="3.5" y="4.5" width="7" height="5" fill="#fff"/><path d="M3.5 4.5 L7 7.3 L10.5 4.5" fill="none" stroke="var(--accent)" stroke-width="0.8"/></svg>
        clara@gildedladle.com
      </li>
      <li class="contacts__item">
        <svg class="contacts__icon" viewBox="0 0 14 14" aria-hidden="true"><circle cx="7" cy="7" r="7" fill="var(--accent)"/><circle cx="7" cy="7" r="3.5" fill="none" stroke="#fff" stroke-width="0.9"/><path d="M3.5 7 H10.5 M7 3.5 V10.5" stroke="#fff" stroke-width="0.8"/></svg>
        www.gildedladle.com
      </li>
    </ul>
  </section>

</main>
</body>
</html>
```